Business Cards for new orthopaedic surgery practice

My husband and I are starting our own orthopaedic surgery practice. We are looking for a business card that is uniform, but one will have my name/title and the other will have his. You can just create one design with my name on it for now. But when I choose your design as the winning design I will ask that you add another copy with his name/title.

We are looking for classy, simple, elite all in one. We like dark blues/a little gold/yellow. Something that goes with our logo. We want our logo incorporated. Here is all the info you need:
Business name: RV Spine & Vitality Center
Location: 38915 North Bramble Ave
Coral Springs, FL 33071
Phone: 954-218-4630
Fax: 954-571-2846
Email: info@myrvspine.example

Names: Lucinda Ferrow, M.D.
Board Certified Hand and Upper Extremity Surgeon

Emeka Dlunga, M.D.
Board Certified Hip & Knee Replacement/General Orthopaedic Surgeon

Can decide what you want to put on the back. Maybe a slogan:
Grounded in Care. Built for You

I am just going to upload our logo. The only thing is if we select you as the winning design, the location, and phone numbers may change. We will need your help to update that once fully solidified.

Industry/Entity Type

Medical

Contact Information for Business Card

Colors
0054AA
0677BA
7BADD7
CADEEF
E8F1F8
0094D4
00A9DD
6FCCEA
C7EBF8
E9F6FB

Requirements
Must have
• class, appeal,
Should not have
• We want to air on the side of masculine if we are looking at masculine vs. feminine feel. But we still want it classy, sophisticated, and something we will love

```html
<!DOCTYPE html>
<html lang="en">
<head>
<meta charset="utf-8">
<title>RV Spine &amp; Vitality Center – Business Card</title>
<link rel="stylesheet" href="https://fonts.googleapis.com/css2?family=Montserrat:wght@500;600;700&display=swap">
<style>
  :root {
    --stage: #3a3a3c;
    --navy: #1b2a5c;
    --navy-deep: #14204a;
    --navy-glow: #2a3f88;
    --gold: #c9a055;
    --paper: #ffffff;
    --ink: #1b2a5c;
  }
  * { box-sizing: border-box; margin: 0; padding: 0; }
  html, body { width: 1200px; height: 900px; overflow: hidden; }
  body {
    background: var(--stage);
    font-family: "Montserrat", Arial, sans-serif;
    position: relative;
  }
  .card {
    position: absolute;
    left: 320px;
    width: 560px;
    height: 320px;
    border-radius: 16px;
    overflow: hidden;
  }
  .card-front { top: 100px; background: var(--paper); color: var(--ink); }
  .card-back  { top: 480px; background: var(--navy); }

  /* front */
  .brand {
    position: absolute; left: 40px; top: 42px;
    display: flex; align-items: center; gap: 12px;
    width: 220px;
  }
  .brand-dot {
    flex: 0 0 auto; width: 20px; height: 20px; border-radius: 50%;
    background: var(--navy);
  }
  .brand-name {
    font-size: 18px; font-weight: 700; line-height: 1.25; color: var(--navy);
  }
  .slogan {
    position: absolute; left: 40px; bottom: 38px;
    font-size: 13px; font-weight: 600; color: var(--ink);
    white-space: nowrap;
  }
  .doctor { position: absolute; left: 290px; top: 40px; }
  .doctor-name {
    font-size: 18px; font-weight: 700; letter-spacing: 0.4px;
    color: var(--gold); text-transform: uppercase; white-space: nowrap;
  }
  .doctor-title {
    margin-top: 6px; font-size: 13px; font-weight: 500; line-height: 1.3;
  }
  .contact-list {
    position: absolute; left: 290px; top: 150px;
    list-style: none; font-size: 12.5px; font-weight: 600; line-height: 1.45;
  }
  .contact-list li { display: flex; align-items: center; gap: 7px; white-space: nowrap; }
  .contact-list svg { width: 11px; height: 11px; flex: 0 0 auto; }
  .web-domain { color: var(--gold); }
  .address {
    position: absolute; left: 290px; bottom: 32px;
    font-size: 12.5px; font-weight: 600; line-height: 1.4; font-style: normal;
    white-space: nowrap;
  }

  /* back */
  .pattern-field {
    position: absolute; inset: 0;
    background: radial-gradient(circle at 85% 60%, var(--navy-glow) 0%, var(--navy) 45%, var(--navy-deep) 100%);
  }
  .back-brand {
    position: absolute; right: 60px; top: 60%; transform: translateY(-50%);
    display: flex; align-items: center; gap: 8px; width: 160px;
  }
  .back-brand .brand-dot { width: 12px; height: 12px; background: var(--paper); }
  .back-brand .brand-name { font-size: 12px; color: var(--paper); }
</style>
</head>
<body>
  <section class="card card-front">
    <div class="brand">
      <span class="brand-dot"></span>
      <span class="brand-name">RV Spine &amp; Vitality Center</span>
    </div>
    <p class="slogan">Grounded in Care. Built for You</p>

    <div class="doctor">
      <h1 class="doctor-name">Lucinda Ferrow, M.D</h1>
      <p class="doctor-title">Board Certified Hand and<br>Upper Extremity Surgeon</p>
    </div>

    <ul class="contact-list">
      <li>
        <svg viewBox="0 0 12 12"><path d="M2.5 1 L4.5 1 L5 3.5 L3.8 4.4 Q4.8 6.8 7.6 8.2 L8.5 7 L11 7.5 L11 9.5 Q11 11 9.5 11 Q1 10 1 2.5 Q1 1 2.5 1 Z" fill="var(--gold)"/></svg>
        954-218-4630
      </li>
      <li>
        <svg viewBox="0 0 12 12"><rect x="2" y="1" width="8" height="4" fill="none" stroke="var(--gold)" stroke-width="1.2"/><rect x="1" y="5" width="10" height="6" rx="1" fill="var(--gold)"/></svg>
        954-571-2846
      </li>
      <li>
        <svg viewBox="0 0 12 12"><rect x="1" y="2.5" width="10" height="7" fill="none" stroke="var(--gold)" stroke-width="1.2"/><path d="M1 2.5 L6 6.5 L11 2.5" fill="none" stroke="var(--gold)" stroke-width="1.2"/></svg>
        info@myrvspine.example
      </li>
      <li>
        <svg viewBox="0 0 12 12"><circle cx="6" cy="6" r="5" fill="none" stroke="var(--gold)" stroke-width="1.2"/><path d="M1 6 H11 M6 1 Q3 6 6 11 M6 1 Q9 6 6 11" fill="none" stroke="var(--gold)" stroke-width="1"/></svg>
        <span>www.<span class="web-domain">myrvspine</span>.example</span>
      </li>
    </ul>

    <address class="address">38915 North Bramble Ave<br>Maple Hollow, FL 34902</address>
  </section>

  <section class="card card-back">
    <div class="pattern-field" role="img" aria-label="Repeating tone-on-tone navy pattern of the practice emblem"></div>
    <div class="back-brand">
      <span class="brand-dot"></span>
      <span class="brand-name">RV Spine &amp; Vitality Center</span>
    </div>
  </section>
</body>
</html>
```